Business card, stationary etc. for management, maintenance company
Tal-Ridge House Services
Business card, stationary etc. for management, maintenance company - Construction
Creative Brief
Professional
Berend Okafor
512 MAPLEWOOD LN NE Fort Walton Beach, FL 32591
talridgehouse@mailbox-demo.net
www.TalRidgeHouse-demo.net
I'd like one side of the card to be only logo, and the rest of the information on the other side. I probably don't want to have the address listed on the card.
TalRidgeHouse TalRidgeHouse
Hello there, thank you for the drafts. Can we do a QR code in the design somehow instead of the address of the business? Thank you

```html
<!DOCTYPE html>
<html lang="en">
<head>
<meta charset="utf-8">
<title>Tal-Ridge House Services – Business Card</title>
<link rel="stylesheet" href="https://fonts.googleapis.com/css2?family=PT+Serif&family=Arimo:wght@400;700&display=swap">
<style>
  :root {
    --backdrop: #1f86cf;
    --card: #1d232d;
    --lime-dark: #8cc61f;
    --lime-light: #c8ef3c;
    --ink-light: #ffffff;
    --ink-muted: #d7dbe2;
    --ink-dark: #1d232d;
  }
  * { margin: 0; padding: 0; box-sizing: border-box; }
  html, body {
    width: 1200px; height: 749px; overflow: hidden;
    background: var(--backdrop);
  }
  .canvas { position: relative; width: 1200px; height: 749px; }
  .card {
    position: absolute; left: 372px; width: 456px; height: 268px;
    background: var(--card); border-radius: 16px; overflow: hidden;
  }
  .card--front { top: 103px; }
  .card--back { top: 405px; }
  .card__band {
    position: absolute; left: 0; right: 0; bottom: 0; height: 30px;
    background: linear-gradient(180deg, var(--lime-light), var(--lime-dark));
    display: flex; align-items: center; justify-content: center;
  }
  .card--back .card__band { height: 26px; }
  .website {
    font-family: "Arimo", sans-serif; font-weight: 700; font-size: 13px;
    color: var(--ink-dark); letter-spacing: 0.2px;
  }
  .divider-tab {
    position: absolute; left: 211px; top: 0; width: 24px; height: 32px;
    background: linear-gradient(180deg, var(--lime-light), var(--lime-dark));
  }
  .divider-line {
    position: absolute; left: 222px; top: 32px; bottom: 30px; width: 2px;
    background: var(--lime-dark);
  }
  .person {
    position: absolute; left: 28px; top: 66px; width: 186px;
    font-family: "PT Serif", serif; font-weight: 400; font-size: 26px;
    line-height: 1.2; white-space: nowrap; color: var(--ink-light);
  }
  .contact { position: absolute; left: 28px; top: 136px; width: 186px; list-style: none; }
  .contact li {
    display: flex; align-items: center; gap: 10px; height: 36px;
    font-family: "Arimo", sans-serif; font-size: 10px; white-space: nowrap;
    color: var(--ink-muted);
  }
  .contact svg { width: 11px; height: 11px; fill: var(--ink-light); flex: none; }
  .brand {
    position: absolute; display: flex; align-items: center; gap: 10px;
    font-family: "Arimo", sans-serif; font-weight: 700; color: var(--ink-light);
    text-transform: uppercase; line-height: 1.15;
  }
  .brand__mark { width: 16px; height: 16px; background: var(--lime-dark); flex: none; }
  .card--front .brand { left: 248px; top: 98px; font-size: 16px; }
  .card--back .brand {
    left: 0; right: 0; top: 96px; justify-content: center; font-size: 21px;
  }
</style>
</head>
<body>
<main class="canvas">
  <section class="card card--front" aria-label="Card front with contact details">
    <div class="divider-tab"></div>
    <div class="divider-line"></div>
    <h1 class="person">Berend Okafor</h1>
    <ul class="contact">
      <li>
        <svg viewBox="0 0 24 24" aria-hidden="true"><path d="M6.6 10.8a15.1 15.1 0 0 0 6.6 6.6l2.2-2.2a1 1 0 0 1 1-.25 11.4 11.4 0 0 0 3.6.6 1 1 0 0 1 1 1V20a1 1 0 0 1-1 1A17 17 0 0 1 3 4a1 1 0 0 1 1-1h3.5a1 1 0 0 1 1 1c0 1.25.2 2.45.6 3.6a1 1 0 0 1-.25 1z"/></svg>
        850-555-0147
      </li>
      <li>
        <svg viewBox="0 0 24 24" aria-hidden="true"><path d="M2 5h20v14H2z M4 7v.5l8 5 8-5V7l-8 5z" fill-rule="evenodd"/></svg>
        talridgehouse@mailbox-demo.net
      </li>
    </ul>
    <div class="brand">
      <span class="brand__mark"></span>
      <span>Tal-Ridge House<br>Services</span>
    </div>
    <div class="card__band"><span class="website">www.talridgehouse-demo.net</span></div>
  </section>

  <section class="card card--back" aria-label="Card back with brand name">
    <div class="brand">
      <span class="brand__mark"></span>
      <span>Tal-Ridge House<br>Services</span>
    </div>
    <div class="card__band"></div>
  </section>
</main>
</body>
</html>
```